Kalm to Bloom: Prespective and Balence in People's Lives Needs a Buissness Card Design

Calm to Bloom Community Center is an organization that seeks to bring balance into people's lives. Main services include: guided meditation, group brainstorming, and guided counseling. Calm to Bloom combines Eastern practices, i.e. Buddhism, Hinduism, and Taoism, with Western practices: therapy, group brainstorming and healing. We would like a double sided card: 1) front vertical with image, 2) back horizontal with information. The main colors for the card are red, white, black. Different finishes would be nice--please no high gloss. Matte, pearlized, embossing--used tactfully and sparingly would be nice. The card should convey balance/harmony in a modern world.

```html
<!DOCTYPE html>
<html lang="en">
<head>
<meta charset="utf-8">
<title>Calm to Bloom Community Center – Business Card</title>
<link rel="stylesheet" href="https://fonts.googleapis.com/css2?family=Arimo:wght@400&family=Bodoni+Moda:wght@400&display=swap">
<style>
  :root {
    --paper: #ffffff;
    --ink: #000000;
    --accent-red: #d80000;
    --label-ink: #000000;
  }
  * { margin: 0; padding: 0; box-sizing: border-box; }
  html, body {
    width: 1200px; height: 900px; overflow: hidden;
    background: var(--paper);
  }
  .sheet { position: relative; width: 1200px; height: 900px; }

  .side-label {
    position: absolute;
    font-family: "Arimo", Arial, sans-serif;
    font-weight: 400;
    font-size: 34px;
    color: var(--label-ink);
    text-align: center;
    line-height: 1;
  }
  .side-label--front { left: 32px; width: 444px; top: 112px; }
  .side-label--back { left: 530px; width: 652px; top: 196px; }

  /* Front – vertical */
  .card-front {
    position: absolute;
    left: 32px; top: 151px;
    width: 426px; height: 639px;
    border: 2px solid var(--ink);
    background: linear-gradient(to right, var(--paper) 0 50%, var(--ink) 50% 100%);
  }
  .card-front__artwork {
    position: absolute;
    left: 105px; top: 211px;
    width: 214px; height: 214px;
    background: var(--accent-red);
  }

  /* Back – horizontal */
  .card-back {
    position: absolute;
    left: 530px; top: 247px;
    width: 641px; height: 428px;
    background: var(--ink);
    color: var(--paper);
    text-align: center;
    font-family: "Bodoni Moda", "Didot", serif;
    font-weight: 400;
  }
  .brand-name {
    position: absolute; left: 0; right: 0; top: 58px;
    font-size: 30px;
    line-height: 1;
  }
  .tagline {
    position: absolute; left: 0; right: 0; top: 140px;
    font-size: 22px;
  }
  .person { position: absolute; left: 0; right: 0; top: 210px; }
  .person__name { font-size: 28px; line-height: 1.1; }
  .person__services { font-size: 13px; margin-top: 2px; }
  .contact {
    position: absolute; left: 0; right: 0; top: 330px;
    font-size: 14.5px; line-height: 21px;
    font-style: normal;
  }
</style>
</head>
<body>
<main class="sheet">
  <h2 class="side-label side-label--front">FRONT SIDE</h2>
  <section class="card-front">
    <div class="card-front__artwork" role="img" aria-label="Artwork area: two mirrored figures in red and white, symbolising balance"></div>
  </section>

  <h2 class="side-label side-label--back">BACK SIDE</h2>
  <section class="card-back">
    <p class="brand-name">Calm to Bloom Community Center</p>
    <p class="tagline">Balance - Harmony</p>
    <div class="person">
      <p class="person__name">A.B. xyz</p>
      <p class="person__services">Meditation-Brainstorming-Counseling</p>
    </div>
    <address class="contact">
      418 Maple Hollow Road 3B Brooklyn, NY 11230 Tel : (555) 014-2736<br>
      Website : www.calmtobloomcenter.org<br>
      Email ID : info@calmtobloomcenter.org
    </address>
  </section>
</main>
</body>
</html>
```